Industrial Company needing new business cards

We are a newly branded Industrial trade company. We specialise in Electrical, Mechanical and Air-conditioning.

I would like to see designs single sided. Focusing on the color scheme white/red/black and possibly gray. Possibly make it a black card with white writting... but open to all designs.

I would like the design to be professional, sleek and to the point.

Industry/Entity Type

Business

Contact Information for Business Card

Tom Harwick
Managing Director / Electrician
tomwork@velnet.com.au
47 Garnet Road, Rutherford NSW 2320
Mobile: 0427115830
www.harwickindustrialgroup.com.au

Requirements
Must have
• Must be able to be sent in a manner that i can change the details for each employee.
• Our logo
Nice to have
• Would like it to somehow have " incorporating Talvo Group Pty Ltd" as this is the company we have taken over.
Should not have
• No yellow!!!
• must not simply place "talvo group" randomly on the business card. refer nice to have.

```html
<!DOCTYPE html>
<html lang="en">
<head>
<meta charset="utf-8">
<title>Harwick Industrial Group – Business Card</title>
<link rel="stylesheet" href="https://fonts.googleapis.com/css2?family=Arimo:wght@400;700&display=swap">
<style>
  :root {
    --red: #e8140f;
    --red-deep: #c70d0a;
    --white: #ffffff;
    --charcoal: #2a2a2a;
    --charcoal-dark: #141414;
    --band-light: #d9d9d9;
    --band-dark: #5a5a5a;
    --ink: #1c1c1c;
  }
  html, body {
    margin: 0;
    padding: 0;
    width: 720px;
    height: 1200px;
    overflow: hidden;
    background: var(--charcoal-dark);
  }
  .card {
    position: relative;
    width: 720px;
    height: 1200px;
    overflow: hidden;
    font-family: "Arimo", Arial, sans-serif;
    background: radial-gradient(ellipse 70% 55% at 50% 25%, #4a4a4a 0%, var(--charcoal) 45%, var(--charcoal-dark) 100%);
  }
  .card__shapes {
    position: absolute;
    inset: 0;
  }
  .contact {
    position: absolute;
    width: 330px;
    margin: 0;
    color: var(--red);
    font-weight: 400;
    text-align: center;
    white-space: nowrap;
    line-height: 1;
  }
  .contact--name { top: 293px; left: 184px; font-size: 31px; }
  .contact--title { top: 346px; left: 197px; font-size: 21px; }
  .contact--email { top: 393px; left: 195px; font-size: 26px; }
  .contact--phone { top: 456px; left: 190px; font-size: 26px; }
  .contact--address { top: 550px; left: 195px; font-size: 26px; line-height: 33px; }
  .contact--web { top: 626px; left: 194px; font-size: 19px; letter-spacing: -0.3px; }

  .brand {
    position: absolute;
    left: 0;
    top: 960px;
    width: 720px;
    height: 190px;
    display: flex;
    align-items: center;
    justify-content: center;
    gap: 26px;
  }
  .brand__mark {
    width: 78px;
    height: 78px;
    background: var(--red);
  }
  .brand__name {
    margin: 0;
    font-size: 44px;
    font-weight: 700;
    line-height: 46px;
    letter-spacing: 1px;
    text-transform: uppercase;
    color: var(--ink);
  }
  .incorporating {
    position: absolute;
    left: 0;
    top: 1151px;
    width: 720px;
    margin: 0;
    text-align: center;
    font-size: 34px;
    color: var(--ink);
    line-height: 1;
  }
</style>
</head>
<body>
<main class="card">
  <svg class="card__shapes" width="720" height="1200" viewBox="0 0 720 1200" aria-hidden="true">
    <defs>
      <radialGradient id="band-glow" cx="50%" cy="55%" r="65%">
        <stop offset="0%" stop-color="#d9d9d9"/>
        <stop offset="55%" stop-color="#a9a9a9"/>
        <stop offset="100%" stop-color="#5a5a5a"/>
      </radialGradient>
      <linearGradient id="band-shadow" x1="0" y1="0" x2="0" y2="1">
        <stop offset="0%" stop-color="#000" stop-opacity="0"/>
        <stop offset="100%" stop-color="#000" stop-opacity="0.35"/>
      </linearGradient>
    </defs>

    <rect class="plate plate--left" x="133" y="350" width="64" height="590" fill="var(--red)"/>
    <polygon class="plate plate--right" points="522,581 551,597 551,940 522,940" fill="var(--red-deep)"/>
    <path class="panel" d="M195 208 Q380 210 524 275 L524 940 L195 940 Z" fill="var(--white)"/>

    <g class="icon icon--mail" fill="none" stroke-width="2.4">
      <rect x="146" y="400" width="37" height="26" fill="#f1f1f1" stroke="#cfcfcf"/>
      <path d="M147 401 L164.5 416 L182 401" stroke="#bdbdbd"/>
      <path d="M147 425 L160 413 M182 425 L169 413" stroke="#bdbdbd"/>
    </g>
    <path class="icon icon--phone" d="M160 451 c-6 3 -8 8 -8 22 s2 19 8 22 l6 -1 c2 -1 2 -3 1 -5 l-2 -6 c-1 -2 -3 -2 -5 -1 c-2 -3 -2 -15 0 -18 c2 1 4 1 5 -1 l2 -6 c1 -2 1 -4 -1 -5 z" fill="#f2f2f2"/>

    <rect x="0" y="915" width="720" height="25" fill="url(#band-shadow)"/>
    <rect class="band" x="0" y="940" width="720" height="260" fill="url(#band-glow)"/>
  </svg>

  <h1 class="contact contact--name">Tom Harwick</h1>
  <p class="contact contact--title">Managing Director/Electrician</p>
  <p class="contact contact--email">tomwork@velnet.com.au</p>
  <p class="contact contact--phone">0427115830</p>
  <p class="contact contact--address">47 Garnet Road<br>Kelvale NSW 2391</p>
  <p class="contact contact--web">www.harwickindustrialgroup.com.au</p>

  <div class="brand">
    <span class="brand__mark"></span>
    <p class="brand__name">Harwick<br>Industrial<br>Group</p>
  </div>

  <p class="incorporating">Incorporating Talvo Group Pty Ltd</p>
</main>
</body>
</html>
```